Harlow Ironworks Business Card

We need a business card design for a new small metal fabrication business in rural NSW, Australia.

The business (Harlow Ironworks) is owner operated by a man with the initials KB - much of the branding comes from this name.

Harlow Ironworks designs, engineers, repairs and manufactures a range of custom, quality metal works including vehicle trays, agricultural machinery impliments, trailers, wood splitters, fire pits, furniture etc.

The brand position focuses on custom work of the highest quality.

Business card design should show quality, attention to detail and stand out among a mass of business cards.

Logos are in the files

The grey color may be changed on the logo if required to stand out more.

There is an image attached of a simple card that is liked because it is clean, clear, simple, masculine and effective. It says 'quality'. As most of the work we do is custom it would be good to have the business card speak to this.

Target Market(s)

Rural and regional based Australians. Primarily adult male 25-60 yrs. Primary production / rural / travelling lifestyle.

Industry/Entity Type

Metal Fabrication

Contact Information for Business Card

The words 'custom quality fabrications' would be great somewhere perhaps on the backside (not on the information side)
Name
title
Phone: 0418 539 746 and (02) 6193 4827
email: info@harlowiw.com.au
www.harlowiw.com.au

address (2 lines)

Requirements
Nice to have
• Background colour should be very navy blue or black.
Should not have
• NO orange and blue combinations.
• Navy is OK

```html
<!DOCTYPE html>
<html lang="en">
<head>
<meta charset="utf-8">
<title>Harlow Ironworks Business Card</title>
<link rel="stylesheet" href="https://fonts.googleapis.com/css2?family=Open+Sans:wght@400;600;700&display=swap">
<style>
  :root {
    --backdrop: #e6e4e0;
    --card-frost: #c8cacb;
    --panel-grey: #a6a9ac;
    --panel-deep: #979a9e;
    --highlight: #e4e6e6;
    --brand-green: #3f9a2c;
    --brand-green-deep: #2f7f22;
    --ink-dark: #3b3d40;
    --text-light: #ffffff;
  }
  html, body {
    margin: 0;
    padding: 0;
    width: 1200px;
    height: 969px;
    overflow: hidden;
    background: var(--backdrop);
    font-family: "Open Sans", Arial, sans-serif;
  }
  .canvas {
    position: relative;
    width: 1200px;
    height: 969px;
  }
  .business-card {
    position: absolute;
    left: 100px;
    top: 200px;
    width: 1000px;
    height: 568px;
    background: var(--card-frost);
    overflow: hidden;
    box-shadow: 0 10px 30px rgba(0,0,0,0.18);
  }
  .card-shapes {
    position: absolute;
    inset: 0;
  }
  .holder {
    position: absolute;
    left: 60px;
    top: 64px;
    color: var(--text-light);
  }
  .holder-name {
    margin: 0;
    font-size: 30px;
    font-weight: 600;
    letter-spacing: 0.5px;
    line-height: 1.2;
  }
  .holder-title {
    margin: 2px 0 0;
    font-size: 24px;
    font-weight: 400;
  }
  .contact-list {
    position: absolute;
    left: 70px;
    top: 350px;
    margin: 0;
    padding: 0;
    list-style: none;
    color: var(--text-light);
    font-size: 24px;
  }
  .contact-list li {
    display: flex;
    align-items: center;
    height: 38px;
  }
  .contact-icon {
    width: 22px;
    height: 22px;
    margin-right: 12px;
    fill: var(--text-light);
    flex: none;
  }
  .brand-lockup {
    position: absolute;
    left: 530px;
    top: 140px;
    width: 360px;
    text-align: center;
  }
  .brand-square {
    display: block;
    width: 110px;
    height: 110px;
    margin: 0 auto 34px;
    background: var(--brand-green);
  }
  .brand-name {
    margin: 0;
    color: var(--ink-dark);
    font-weight: 700;
    text-transform: uppercase;
    line-height: 1.05;
  }
  .brand-name .line-main {
    display: block;
    font-size: 58px;
    letter-spacing: 6px;
  }
  .brand-name .line-sub {
    display: block;
    font-size: 30px;
    letter-spacing: 7px;
  }
</style>
</head>
<body>
<div class="canvas">
  <section class="business-card" aria-label="Harlow Ironworks business card">
    <svg class="card-shapes" width="1000" height="568" viewBox="0 0 1000 568" aria-hidden="true">
      <!-- left information panel -->
      <polygon points="0,0 455,0 455,568 0,568" fill="var(--panel-grey)"/>
      <polygon points="0,0 310,0 310,138 0,138" fill="var(--panel-deep)" opacity="0.5"/>
      <!-- light diagonal accents -->
      <polygon points="310,138 455,0 455,138" fill="var(--highlight)" opacity="0.85"/>
      <polygon points="455,0 455,138 530,138 650,0" fill="var(--highlight)" opacity="0.35"/>
      <!-- green corners -->
      <polygon points="853,0 1000,0 1000,138" fill="var(--brand-green)"/>
      <polygon points="800,0 853,0 1000,138 1000,190" fill="var(--highlight)" opacity="0.45"/>
      <polygon points="1000,405 1000,568 836,568" fill="var(--brand-green-deep)"/>
    </svg>

    <header class="holder">
      <h1 class="holder-name">KIERAN BLAKE</h1>
      <p class="holder-title">CEO/Founder</p>
    </header>

    <ul class="contact-list">
      <li>
        <svg class="contact-icon" viewBox="0 0 24 24" aria-hidden="true"><path d="M6.6 10.8a15.1 15.1 0 0 0 6.6 6.6l2.2-2.2a1 1 0 0 1 1-.25 11.4 11.4 0 0 0 3.6.6 1 1 0 0 1 1 1V20a1 1 0 0 1-1 1A17 17 0 0 1 3 4a1 1 0 0 1 1-1h3.5a1 1 0 0 1 1 1c0 1.25.2 2.45.6 3.6a1 1 0 0 1-.25 1z"/></svg>
        0418 539 746
      </li>
      <li>
        <svg class="contact-icon" viewBox="0 0 24 24" aria-hidden="true"><path d="M6.6 10.8a15.1 15.1 0 0 0 6.6 6.6l2.2-2.2a1 1 0 0 1 1-.25 11.4 11.4 0 0 0 3.6.6 1 1 0 0 1 1 1V20a1 1 0 0 1-1 1A17 17 0 0 1 3 4a1 1 0 0 1 1-1h3.5a1 1 0 0 1 1 1c0 1.25.2 2.45.6 3.6a1 1 0 0 1-.25 1z"/></svg>
        (02) 6193 4827
      </li>
      <li>
        <svg class="contact-icon" viewBox="0 0 24 24" aria-hidden="true"><path d="M2 5h20v14H2z M3.5 6.5 12 13l8.5-6.5" fill="none" stroke="#fff" stroke-width="2"/></svg>
        info@harlowiw.com.au
      </li>
      <li>
        <svg class="contact-icon" viewBox="0 0 24 24" aria-hidden="true"><circle cx="12" cy="12" r="9.5" fill="none" stroke="#fff" stroke-width="2"/><path d="M2.5 12h19M12 2.5c-3 3-3 16 0 19M12 2.5c3 3 3 16 0 19" fill="none" stroke="#fff" stroke-width="1.6"/></svg>
        www.harlowiw.com.au
      </li>
    </ul>

    <div class="brand-lockup">
      <span class="brand-square" aria-hidden="true"></span>
      <p class="brand-name"><span class="line-main">Harlow</span><span class="line-sub">Ironworks</span></p>
    </div>
  </section>
</div>
</body>
</html>
```